Create a professional, eye-catching business card design that reflects the values and services of Brookfern Veterinary Hospital. we provide veterinary services and the business card should be a memorable representation of the clinic and align with its branding and mission. our tag line is "Life Long Companions, Lifelong Care"
Use clean, modern typography. Prioritize readability and professionalism. We would like to see designs that use the color blue, as in the logo example. the final design should communicate professionalism and care, with attention to detail.

```html
<!DOCTYPE html>
<html lang="en">
<head>
<meta charset="UTF-8">
<title>Brookfern Veterinary Hospital – Business Card</title>
<link href="https://fonts.googleapis.com/css2?family=Montserrat:wght@600;700;800&display=swap" rel="stylesheet">
<style>
  :root {
    --navy: #1e3163;
    --navy-deep: #172750;
    --navy-photo: #22376e;
    --white: #ffffff;
    --stage: #8c8c8c;
  }
  * { margin: 0; padding: 0; box-sizing: border-box; }
  html, body {
    width: 976px; height: 1200px; overflow: hidden;
    background: var(--stage);
    font-family: "Montserrat", Arial, sans-serif;
  }
  .card {
    position: absolute; left: 92px;
    width: 792px; height: 453px;
    border-radius: 45px; overflow: hidden;
    background: var(--white);
  }
  .card--front { top: 91px; }
  .card--back { top: 655px; }
  .card svg.shape { position: absolute; inset: 0; }

  /* front */
  .front-brand {
    position: absolute; left: 0; right: 0; top: 130px;
    text-align: center; color: var(--white);
  }
  .brand-circle {
    width: 120px; height: 120px; margin: 0 auto 14px;
    border: 2px solid var(--white); border-radius: 50%;
  }
  .brand-name {
    font-weight: 800; font-size: 40px; line-height: 1; letter-spacing: 0.5px;
  }
  .brand-sub {
    font-weight: 800; font-size: 14.5px; line-height: 1.2; margin-top: 4px; letter-spacing: 0.3px;
  }

  /* back */
  .holder {
    position: absolute; left: 63px; top: 64px; color: var(--navy);
  }
  .holder-name { font-weight: 800; font-size: 45px; line-height: 1; }
  .holder-role { font-weight: 600; font-size: 15px; letter-spacing: 2.6px; margin-top: 8px; }
  .holder-rule { width: 190px; height: 2px; background: var(--navy); margin-top: 14px; }

  .contacts { position: absolute; left: 69px; top: 206px; list-style: none; }
  .contact {
    display: flex; align-items: center; height: 28px; margin-bottom: 34px;
    color: var(--navy); font-weight: 600; font-size: 18px; letter-spacing: 0.4px;
  }
  .contact-icon {
    width: 28px; height: 28px; border-radius: 50%; background: var(--navy);
    display: flex; align-items: center; justify-content: center; margin-right: 20px; flex: none;
  }
  .back-brand {
    position: absolute; left: 470px; width: 248px; top: 130px;
    text-align: center; color: var(--navy);
  }
  .back-brand .brand-circle { border-color: var(--navy); width: 112px; height: 112px; }
  .back-brand .brand-name { font-size: 36px; }
  .back-brand .brand-sub { font-size: 13px; }
</style>
</head>
<body>

<section class="card card--front">
  <svg class="shape" viewBox="0 0 792 453" role="img" aria-label="Photo of a kitten and a puppy held by a veterinarian's gloved hands, tinted navy blue">
    <defs>
      <linearGradient id="photoTint" x1="0" y1="0" x2="1" y2="1">
        <stop offset="0" stop-color="#1b2d5f"/>
        <stop offset="0.5" stop-color="#2a3f78"/>
        <stop offset="1" stop-color="#1a2b5a"/>
      </linearGradient>
    </defs>
    <path d="M0 0 H555 C680 5 780 110 792 215 V453 H230 C110 420 20 340 0 220 Z" fill="url(#photoTint)"/>
  </svg>
  <div class="front-brand">
    <div class="brand-circle"></div>
    <div class="brand-name">BROOKFERN</div>
    <div class="brand-sub">VETERINARY HOSPITAL</div>
  </div>
</section>

<section class="card card--back">
  <svg class="shape" viewBox="0 0 792 453" aria-hidden="true">
    <path d="M548 0 H792 V420 C760 260 700 60 548 0 Z" fill="var(--navy)"/>
    <path d="M0 220 C20 330 120 425 250 453 H0 Z" fill="var(--navy)"/>
  </svg>

  <div class="holder">
    <div class="holder-name">BROOKFERN</div>
    <div class="holder-role">DESIGNATION</div>
    <div class="holder-rule"></div>
  </div>

  <ul class="contacts">
    <li class="contact">
      <span class="contact-icon">
        <svg width="14" height="14" viewBox="0 0 24 24"><path fill="#fff" d="M6.6 10.8a15.1 15.1 0 0 0 6.6 6.6l2.2-2.2a1 1 0 0 1 1-.25 11.4 11.4 0 0 0 3.6.57 1 1 0 0 1 1 1V20a1 1 0 0 1-1 1A17 17 0 0 1 3 4a1 1 0 0 1 1-1h3.5a1 1 0 0 1 1 1c0 1.25.2 2.45.57 3.57a1 1 0 0 1-.25 1z"/></svg>
      </span>+070 5550 31927
    </li>
    <li class="contact">
      <span class="contact-icon">
        <svg width="14" height="14" viewBox="0 0 24 24"><rect x="3" y="5" width="18" height="14" rx="1.5" fill="none" stroke="#fff" stroke-width="2"/><path d="M3 6l9 7 9-7" fill="none" stroke="#fff" stroke-width="2"/></svg>
      </span>hello@brookfernvet.com
    </li>
    <li class="contact">
      <span class="contact-icon">
        <svg width="16" height="16" viewBox="0 0 24 24" fill="none" stroke="#fff" stroke-width="1.8"><circle cx="12" cy="12" r="9"/><ellipse cx="12" cy="12" rx="4" ry="9"/><path d="M3 12h18M5 7h14M5 17h14"/></svg>
      </span>www.brookfernvet.com
    </li>
  </ul>

  <div class="back-brand">
    <div class="brand-circle"></div>
    <div class="brand-name">BROOKFERN</div>
    <div class="brand-sub">VETERINARY HOSPITAL</div>
  </div>
</section>

</body>
</html>
```